Interior Decorating and Event Styling Business Card Design

We need a business card design for a bespoke interior decorating and event styling business, mostly weddings. We also do custom paint finishes and painted floor finishes. We want something simple, organic and stylish with good colour tones used.

On our card we would like our services listed like so -

Interior Decorating
Wedding and Event Styling
Bespoke furniture paint finishes
Painted floor finishes

Industry/Entity Type

Paint

Contact Information for Business Card

Mabel & Moss Design
Rosalind 0487315026
Petra 0439572604
rosalind.carver@mailbrook.com.au
petraloom@tmv4.com.au

```html
<!DOCTYPE html>
<html lang="en">
<head>
<meta charset="utf-8">
<title>Mabel &amp; Moss Design – Business Card Options</title>
<link href="https://fonts.googleapis.com/css2?family=Federo&family=Didact+Gothic&family=Mulish:wght@700&display=swap" rel="stylesheet">
<style>
  :root {
    --page-bg: #ffffff;
    --label-ink: #222222;
    --ink-light: #f4f2e8;
    --band-forest: #4b4f3e;
    --band-sage: #8a8462;
    --band-olive: #737646;
    --leaf-a: #8fa05a;
    --leaf-b: #c9cf9a;
    --leaf-c: #5f8a7a;
    --plaid-a: #6e6a52;
    --plaid-b: #8c7560;
    --damask-a: #e6e2cf;
    --damask-b: #b9b8a2;
    --paisley-a: #c9b48a;
    --paisley-b: #a9c6c6;
    --stripe-ground: #a2aa6c;
    --stripe-line: #eef0dc;
    --lace-a: #d9c79d;
    --lace-b: #c6b283;
  }
  * { margin: 0; padding: 0; box-sizing: border-box; }
  html, body {
    width: 1200px; height: 797px; overflow: hidden;
    background: var(--page-bg);
  }
  .sheet { position: relative; width: 1200px; height: 797px; }

  .option-number {
    position: absolute;
    font-family: "Didact Gothic", Arial, sans-serif;
    font-size: 20px; color: var(--label-ink);
  }

  .card {
    position: absolute; overflow: hidden;
    width: 521px; height: 312px;
    box-shadow: 0 14px 12px -10px rgba(0,0,0,.35);
  }
  .card-pattern, .card-band, .card-border { position: absolute; left: 0; width: 100%; }

  .card-band {
    display: flex; flex-direction: column; align-items: center;
    color: var(--ink-light);
  }
  .brand-name {
    font-family: "Federo", "Trebuchet MS", sans-serif;
    font-size: 40px; font-weight: 400; letter-spacing: .5px;
    margin-top: 14px; line-height: 1.1;
  }
  .service-list {
    font-family: "Didact Gothic", "Century Gothic", sans-serif;
    font-size: 16.5px; line-height: 31px; text-align: center;
    margin-top: 6px; list-style: none;
  }
  .service-list .dot { font-size: 13px; margin: 0 6px; position: relative; top: -1px; }

  /* option 1 */
  .leaf-print {
    top: 0; height: 105px;
    background: linear-gradient(100deg, var(--leaf-a) 0%, var(--leaf-b) 30%, var(--leaf-c) 55%, var(--leaf-a) 75%, var(--leaf-b) 100%);
  }
  .band-forest { top: 105px; height: 145px; background: var(--band-forest); }
  .plaid-border {
    top: 250px; height: 62px;
    background: linear-gradient(180deg, var(--plaid-a), var(--plaid-b) 50%, var(--plaid-a));
  }

  .contact-band { top: 105px; height: 145px; background: var(--band-forest); color: var(--ink-light); }
  .contact {
    position: absolute; top: 32px;
    font-family: "Didact Gothic", "Century Gothic", sans-serif;
    font-size: 15.5px;
  }
  .contact-left { left: 30px; }
  .contact-right { right: 40px; text-align: right; }
  .contact-name {
    font-family: "Mulish", Arial, sans-serif; font-weight: 700;
    font-size: 16.5px; display: block; margin-bottom: 6px;
  }
  .contact-left .contact-name { margin-left: 24px; }
  .contact-line { display: flex; align-items: center; gap: 5px; height: 27px; }
  .contact-right .contact-line { justify-content: flex-end; }
  .contact-line.email { font-size: 14.5px; }
  .icon { width: 15px; height: 15px; flex: none; }

  /* option 2 */
  .damask-print {
    top: 0; height: 105px;
    background: linear-gradient(100deg, var(--damask-b) 0%, var(--damask-a) 35%, var(--damask-b) 65%, var(--damask-a) 100%);
  }
  .band-sage { top: 105px; height: 143px; background: var(--band-sage); }
  .stripe-border {
    top: 248px; height: 60px;
    background: repeating-linear-gradient(90deg, var(--stripe-ground) 0 7px, var(--stripe-line) 7px 9px);
  }

  /* option 3 */
  .paisley-print {
    top: 0; height: 112px;
    background: linear-gradient(100deg, var(--paisley-a) 0%, var(--paisley-b) 25%, var(--paisley-a) 50%, var(--paisley-b) 75%, var(--paisley-a) 100%);
  }
  .band-olive { top: 112px; height: 145px; background: var(--band-olive); }
  .lace-border {
    top: 257px; height: 55px;
    background: linear-gradient(180deg, var(--lace-b), var(--lace-a) 50%, var(--lace-b));
  }
</style>
</head>
<body>
<main class="sheet">

  <span class="option-number" style="left:14px; top:46px;">1</span>
  <span class="option-number" style="left:26px; top:418px;">2</span>
  <span class="option-number" style="left:591px; top:418px;">3</span>

  <!-- Option 1 front -->
  <section class="card" style="left:59px; top:40px; height:312px; width:520px;">
    <div class="card-pattern leaf-print" role="img" aria-label="Green and teal botanical leaf fabric print"></div>
    <div class="card-band band-forest">
      <h1 class="brand-name">Mabel &amp; Moss Design</h1>
      <ul class="service-list">
        <li>Interior Decorating <span class="dot">●</span> Wedding and Event Styling</li>
        <li>Bespoke furniture paint finishes <span class="dot">●</span> Painted floor finishes</li>
      </ul>
    </div>
    <div class="card-border plaid-border" role="img" aria-label="Muted olive and rose plaid fabric border"></div>
  </section>

  <!-- Option 1 back -->
  <section class="card" style="left:628px; top:40px; height:312px; width:521px;">
    <div class="card-pattern leaf-print" role="img" aria-label="Green and teal botanical leaf fabric print"></div>
    <div class="card-band contact-band">
      <div class="contact contact-left">
        <span class="contact-name">Rosalind</span>
        <div class="contact-line">
          <svg class="icon" viewBox="0 0 16 16"><path d="M4 1.5 6 4.5 4.7 6a8 8 0 0 0 5.3 5.3L11.5 10l3 2-1 2.3C7.5 14.5 1.5 8.5 1.7 2.5Z" fill="none" stroke="currentColor" stroke-width="1.3" stroke-linejoin="round"/></svg>
          <span>0487315026</span>
        </div>
        <div class="contact-line email">
          <svg class="icon" viewBox="0 0 16 16"><rect x="1.5" y="3.5" width="13" height="9" fill="none" stroke="currentColor" stroke-width="1.2"/><path d="M1.5 3.5 8 9l6.5-5.5" fill="none" stroke="currentColor" stroke-width="1.2"/></svg>
          <span>rosalind.carver@mailbrook.com.au</span>
        </div>
      </div>
      <div class="contact contact-right">
        <span class="contact-name">Petra</span>
        <div class="contact-line">
          <svg class="icon" viewBox="0 0 16 16"><path d="M4 1.5 6 4.5 4.7 6a8 8 0 0 0 5.3 5.3L11.5 10l3 2-1 2.3C7.5 14.5 1.5 8.5 1.7 2.5Z" fill="none" stroke="currentColor" stroke-width="1.3" stroke-linejoin="round"/></svg>
          <span>0439572604</span>
        </div>
        <div class="contact-line email">
          <svg class="icon" viewBox="0 0 16 16"><rect x="1.5" y="3.5" width="13" height="9" fill="none" stroke="currentColor" stroke-width="1.2"/><path d="M1.5 3.5 8 9l6.5-5.5" fill="none" stroke="currentColor" stroke-width="1.2"/></svg>
          <span>petraloom@tmv4.com.au</span>
        </div>
      </div>
    </div>
    <div class="card-border plaid-border" role="img" aria-label="Muted olive and rose plaid fabric border"></div>
  </section>

  <!-- Option 2 -->
  <section class="card" style="left:59px; top:420px; height:308px; width:520px;">
    <div class="card-pattern damask-print" role="img" aria-label="Pale grey and cream floral damask fabric print"></div>
    <div class="card-band band-sage">
      <h1 class="brand-name">Mabel &amp; Moss Design</h1>
      <ul class="service-list">
        <li>Interior Decorating <span class="dot">●</span> Wedding and Event Styling</li>
        <li>Bespoke furniture paint finishes <span class="dot">●</span> Painted floor finishes</li>
      </ul>
    </div>
    <div class="card-border stripe-border"></div>
  </section>

  <!-- Option 3 -->
  <section class="card" style="left:618px; top:416px; height:312px; width:521px;">
    <div class="card-pattern paisley-print" role="img" aria-label="Tan and duck-egg blue paisley fabric print"></div>
    <div class="card-band band-olive">
      <h1 class="brand-name">Mabel &amp; Moss Design</h1>
      <ul class="service-list">
        <li>Interior Decorating <span class="dot">●</span> Wedding and Event Styling</li>
        <li>Bespoke furniture paint finishes <span class="dot">●</span> Painted floor finishes</li>
      </ul>
    </div>
    <div class="card-border lace-border" role="img" aria-label="Soft beige tone-on-tone paisley fabric border"></div>
  </section>

</main>
</body>
</html>
```